An A2 office artwork piece with quote overlay

I would like a piece of A2 office artwork, inspired by two things important to me and my business, overlaid with a quote. I have attached some photos and I have the quote I would like. My office is dark, minimalistic and modern in design (photo attached). I would like the artwork to contain some element of colour, but it should not be bright, the quote should be the main element with the photo and further design elements creating a subtle background.

The art will go on the wall behind my office chair and will appear in most of my online business video content, therefore I would like it to be inspiring.

The quote to be used:

"It is not because things are difficult that we do not dare; it is because we do not dare that they are difficult." - Talvio

The property in the attached photograph is one we purchased recently and is an important milestone in my business.

I would also like an aviation reference to feature in the background as this was my career before I started my property business and I'm currently training to be a flying instructor. I have attached some aircraft photos which I have taken and I've attached some other items for inspiration. I am open to how the aviation reference is blended in.

Target Market(s)

This isn't a sales piece, it just needs to be intriguing.

Industry/Entity Type

Real estate

Font styles to use
Serif
Sans Serif
Script

Requirements
Must have
• Must have the building in the attached photograph and the quote.
Nice to have
• An aviation reference if this can be blended within the background.
Should not have
• Too many bright colours

```html
<!DOCTYPE html>
<html lang="en">
<head>
<meta charset="utf-8">
<title>Quote artwork – Talvio</title>
<link rel="stylesheet" href="https://fonts.googleapis.com/css2?family=Roboto:wght@400&family=Dancing+Script:wght@500&display=swap">
<style>
  :root {
    --backdrop: #2e2e2f;
    --poster: #1b1b1c;
    --frame-gold: #8c6b40;
    --script-gold: #c39a5c;
    --quote-white: #f4f2ee;
    --sketch-tone: #2a2824;
    --sketch-warm: #3a3226;
    --gauge-dark: #2b2b2c;
    --gauge-mid: #4a4a4c;
  }
  * { box-sizing: border-box; margin: 0; padding: 0; }
  html, body {
    width: 1200px; height: 755px; overflow: hidden;
    background: var(--backdrop);
  }
  .artwork {
    position: absolute;
    left: 348px; top: 20px;
    width: 504px; height: 715px;
    background: var(--poster);
    border: 5px solid var(--frame-gold);
    overflow: hidden;
  }
  .layer { position: absolute; }
  .building-sketch {
    left: 0; right: 0; top: 392px; bottom: 0;
    background: linear-gradient(180deg, rgba(42,40,36,0) 0%, var(--sketch-tone) 35%, #252422 100%);
  }
  .plane-sketch { border-radius: 40% / 50%; }
  .plane-top { left: 345px; top: 8px; width: 142px; height: 46px;
    background: radial-gradient(ellipse, rgba(90,90,95,.35), rgba(90,90,95,0) 70%); }
  .plane-left { left: 2px; top: 171px; width: 218px; height: 61px;
    background: radial-gradient(ellipse, rgba(120,95,60,.35), rgba(120,95,60,0) 70%); }
  .plane-right { left: 300px; top: 296px; width: 190px; height: 56px;
    background: radial-gradient(ellipse, rgba(90,95,105,.35), rgba(90,95,105,0) 70%); }
  .plane-bottom { left: 140px; top: 595px; width: 227px; height: 70px;
    background: radial-gradient(ellipse, rgba(130,130,135,.3), rgba(130,130,135,0) 70%); }
  .gauge-row {
    position: absolute; top: 34px; left: 0; right: 0;
    display: flex; justify-content: center; gap: 10px;
  }
  .gauge {
    width: 85px; height: 85px; border-radius: 50%;
    background: radial-gradient(circle at 50% 45%, var(--gauge-mid), var(--gauge-dark) 70%, #1f1f20 100%);
    box-shadow: 0 0 0 3px #3a3a3b;
  }
  .quote { position: absolute; inset: 0; text-align: center; }
  .line {
    position: absolute; left: 0; right: 0;
    transform: translateY(-50%);
    line-height: 1; white-space: nowrap;
  }
  .sans { font-family: "Roboto", Arial, sans-serif; color: var(--quote-white); font-size: 38px; }
  .script { font-family: "Dancing Script", cursive; color: var(--script-gold); }
  .script.large { font-size: 84px; }
  .script.medium { font-size: 60px; }
  .attribution { font-family: "Roboto", Arial, sans-serif; color: var(--quote-white); font-size: 29px; }
</style>
</head>
<body>
  <main class="artwork">
    <div class="layer building-sketch" role="img" aria-label="Faint line sketch of the recently purchased property building"></div>
    <div class="layer plane-sketch plane-top" role="img" aria-label="Faint line drawing of a light aircraft"></div>
    <div class="layer plane-sketch plane-left" role="img" aria-label="Faint gold sketch of a twin-engine aircraft"></div>
    <div class="layer plane-sketch plane-right" role="img" aria-label="Faint sketch of a twin-engine aircraft"></div>
    <div class="layer plane-sketch plane-bottom" role="img" aria-label="Line drawing of a light aircraft in flight"></div>

    <div class="gauge-row">
      <div class="gauge" role="img" aria-label="Airspeed indicator instrument"></div>
      <div class="gauge" role="img" aria-label="Attitude indicator instrument"></div>
      <div class="gauge" role="img" aria-label="Altimeter instrument"></div>
    </div>

    <blockquote class="quote">
      <p class="line sans" style="top:150px">It is not because</p>
      <p class="line sans" style="top:184px">things are</p>
      <p class="line script large" style="top:236px">difficult</p>
      <p class="line sans" style="top:295px">that we do not</p>
      <p class="line script medium" style="top:341px">dare;</p>
      <p class="line sans" style="top:375px">it is because we do not</p>
      <p class="line script medium" style="top:421px">dare;</p>
      <p class="line sans" style="top:470px">that they are</p>
      <p class="line script large" style="top:522px">difficult</p>
      <cite class="line attribution" style="top:574px; font-style:normal">Talvio</cite>
    </blockquote>
  </main>
</body>
</html>
```